Retro Label for old fashioned soda

We need a label for soda we are having private labeled for our retro, 1950's ice cream shop www.thefrostyparlor.net I don't want the label to look like something from 2017 with a retro feel, but more like an original (possibly kinda cheesy) label you'd see from the 1950's with some of the old catch lines like "tastes great", "invigorating" or "it is refreshing!" The prominent brand should be the name of our ice cream shop, The Frosty Parlor. the soda is also pure cane sugar so it might be good to have that on somewhere

Label size is 2.4" wide by 4" tall. Here is an example of some retro labels from lookfindr. I attached on file to this contest but there are more here: https://www.lookfindr.net/results?q=retro+soda+label&id=8Hq2Lm4Pz7Vb1Kc9Xw3Rt6Yd0Ns5Jf2Ga8Ue4Ko1Mi7Bl3Wp9Dv6Qx2Hc5Zr0Ty8Fn4#img=Pk7Rw2Lx9Qm3:

The label will be the same for all the flavors with the exception of the flavor name changing somewhere on the label. These are the flavors

Root Beer
Orange
Black Cherry
Lemonade
Raspberry Lime -Rickey
White Birch Beer
Lemon Iced Tea
Vanilla Cream
Orange Cream
Sarsaparilla
Ginger Ale

• retro feel. authentic old fashioned look

```html
<!DOCTYPE html>
<html lang="en">
<head>
<meta charset="utf-8">
<title>The Frosty Parlor – Lemonade Soda Label</title>
<link rel="stylesheet" href="https://fonts.googleapis.com/css2?family=Yellowtail&family=Rokkitt:wght@400;500&display=swap">
<style>
  :root {
    --paper: #ffffff;
    --cream: #f6e8cf;
    --sky: #8da4b1;
    --tangerine: #e5895b;
    --cocoa: #6a615b;
    --ink-blue: #1f5f98;
    --flavor-ink: #1d4d7c;
  }
  html, body {
    margin: 0;
    padding: 0;
    width: 1200px;
    height: 1200px;
    overflow: hidden;
    background: var(--paper);
  }
  .canvas {
    position: relative;
    width: 1200px;
    height: 1200px;
  }
  .soda-label {
    position: absolute;
    left: 299px;
    top: 100px;
    width: 602px;
    height: 1000px;
    display: block;
  }
  .script { font-family: "Yellowtail", cursive; }
  .slab { font-family: "Rokkitt", serif; }
  .brand-name { fill: var(--cocoa); }
  .tagline-cane { fill: var(--cream); font-size: 24px; letter-spacing: 0.5px; }
  .catchline { fill: var(--ink-blue); }
  .flavor-name { fill: var(--flavor-ink); font-size: 33px; font-weight: 500; letter-spacing: 0.5px; }
  .fizz circle { fill: var(--cream); }
</style>
</head>
<body>
<main class="canvas">
  <svg class="soda-label" viewBox="0 0 532 883" xmlns="http://www.w3.org/2000/svg" aria-label="The Frosty Parlor lemonade soda label">
    <rect class="label-base" x="0" y="0" width="532" height="883" fill="var(--cream)"/>

    <polygon class="band-top" points="22,21 510,21 510,125 22,221" fill="var(--sky)"/>
    <polygon class="band-stripe" points="22,262 510,166 510,492 22,588" fill="var(--tangerine)"/>
    <path class="brand-panel" fill="var(--cream)"
      d="M97,269 L438,204 Q468,198 468,228 L468,450 Q468,476 442,481 L95,547 Q67,552 67,524 L67,302 Q67,275 97,269 Z"/>

    <polygon class="band-bottom" points="22,668 510,572 510,862 22,862" fill="var(--sky)"/>

    <text class="slab tagline-cane" x="493" y="52" text-anchor="end">pure cane sugar</text>

    <g class="brand-name script">
      <text x="98" y="330" font-size="54">the</text>
      <text x="168" y="410" font-size="88">Frosty</text>
      <text x="98" y="482" font-size="88">Parlor</text>
    </g>

    <g class="catchline script" transform="rotate(-16 420 560)">
      <text x="462" y="522" font-size="26">it's</text>
      <text x="318" y="582" font-size="40">refreshing!</text>
    </g>

    <g class="fizz">
      <circle cx="470" cy="597" r="9"/>
      <circle cx="464" cy="667" r="14"/>
      <circle cx="271" cy="661" r="6"/>
      <circle cx="281" cy="682" r="5"/>
      <circle cx="40" cy="708" r="7"/>
      <circle cx="57" cy="685" r="5"/>
      <circle cx="50" cy="737" r="6"/>
      <circle cx="41" cy="777" r="6"/>
      <circle cx="55" cy="810" r="6"/>
      <circle cx="42" cy="843" r="10"/>
      <circle cx="260" cy="813" r="9"/>
      <circle cx="297" cy="848" r="7"/>
      <circle cx="484" cy="721" r="6"/>
      <circle cx="498" cy="758" r="6"/>
      <circle cx="475" cy="792" r="6"/>
      <circle cx="494" cy="845" r="11"/>
    </g>

    <g class="flavor-badge">
      <rect x="79" y="698" width="373" height="75" rx="37.5" fill="var(--cream)" stroke="var(--ink-blue)" stroke-width="4"/>
      <text class="slab flavor-name" x="265.5" y="746" text-anchor="middle">Lemonade</text>
    </g>
  </svg>
</main>
</body>
</html>
```